Occupational Therapy Clinic Advertisement

Create an advertisement for a magazine. Below I have attached my original ad (Ad 2020.pdf) . I want the ad changed and it should be eye catching. I would like a eye catching graphics added in the ad. It should be a graphic image that applies to education. I am attaching a sample graphic image of that I liked from someone elses ad- it should not be the same- it just is there to show what I like. Please use the same words from my original ad.Dimensions: 3.75in x 10.3 in

Target Market(s)

Parents of School aged children

Requirements
Must have
• Must have eye catching Graphic. Colors should be eye catching for a typed magazine.

```html
<!DOCTYPE html>
<html lang="en">
<head>
<meta charset="utf-8">
<title>Bright Path OT Services</title>
<link href="https://fonts.googleapis.com/css2?family=Oswald:wght@300;400;500;600&display=swap" rel="stylesheet">
<style>
  :root {
    --backdrop: #000000;
    --sky-top: #7ccbe3;
    --sky-bottom: #c9e9f3;
    --navy: #24337a;
    --white: #ffffff;
    --magenta: #e6007e;
    --yellow: #ffed00;
    --green: #43a838;
    --orange: #ee7a0d;
    --light-blue: #5fc3e4;
    --mist: #eaf6fc;
  }
  * { margin: 0; padding: 0; box-sizing: border-box; }
  html, body {
    width: 1200px; height: 1200px; overflow: hidden;
    background: var(--backdrop);
    font-family: "Oswald", "Arial Narrow", sans-serif;
  }
  .ad {
    position: absolute; left: 468px; top: 238px;
    width: 264px; height: 725px;
    background: linear-gradient(to bottom, var(--mist) 0%, var(--white) 55%, var(--white) 100%);
    overflow: hidden;
  }
  .ad > * { position: absolute; }
  .center-line { left: 0; width: 100%; text-align: center; }

  .masthead {
    left: 0; top: 0; width: 100%; height: 132px;
    background: linear-gradient(to bottom, var(--sky-top), var(--sky-bottom));
  }
  .brand-name { top: 9px; font-size: 33px; font-weight: 600; color: var(--white); letter-spacing: -0.3px; line-height: 1.3; }
  .brand-sub { top: 60px; font-size: 24px; font-weight: 400; color: var(--navy); line-height: 1; letter-spacing: -0.5px; }
  .brand-phone { top: 84px; font-size: 31px; font-weight: 400; color: var(--navy); line-height: 1; letter-spacing: -0.8px; }

  .question {
    left: 0; width: 100%; height: 40px;
    display: flex; align-items: center; justify-content: center; text-align: center;
    font-size: 12.5px; font-weight: 400; line-height: 15px;
  }
  .question--pink { top: 132px; background: var(--magenta); color: var(--white); }
  .question--yellow { top: 172px; background: var(--yellow); color: var(--navy); }
  .question--green { top: 212px; background: var(--green); color: var(--white); }

  .promise {
    top: 260px; font-size: 25px; font-weight: 400; color: var(--orange);
    line-height: 30px; letter-spacing: -0.4px;
  }
  .promise .struck { color: var(--light-blue); position: relative; }
  .promise .struck::after {
    content: ""; position: absolute; left: -2px; right: -2px; top: 50%;
    height: 1px; background: var(--navy); transform: rotate(-42deg);
  }

  .service { width: 92px; text-align: center; z-index: 2; }
  .service--evaluate { left: 12px; top: 332px; }
  .service--treat { left: 160px; top: 332px; }
  .service-title { font-size: 15.5px; font-weight: 500; color: var(--magenta); line-height: 20px; letter-spacing: -0.3px; white-space: nowrap; }
  .service-text { font-size: 11.5px; font-weight: 300; color: var(--navy); line-height: 15px; white-space: nowrap; }

  .pencil-art { left: 92px; top: 384px; width: 80px; height: 164px; }

  .approach { top: 560px; font-size: 14px; font-weight: 300; color: var(--orange); line-height: 20px; }

  .rsa-pill {
    left: 58px; top: 589px; width: 145px; height: 20px; border-radius: 10px;
    background: var(--magenta); color: var(--white);
    font-size: 12.5px; font-weight: 300; line-height: 20px; text-align: center;
  }

  .details { top: 613px; font-size: 9.5px; font-weight: 300; color: var(--navy); line-height: 14.5px; }

  .footer-band {
    left: 0; top: 680px; width: 100%; height: 45px; background: var(--orange);
    color: var(--white); text-align: center; font-size: 14.5px; font-weight: 400; line-height: 17.5px;
    padding-top: 4px;
  }
</style>
</head>
<body>
  <div class="ad">
    <div class="masthead"></div>
    <h1 class="brand-name center-line">BRIGHT PATH</h1>
    <p class="brand-sub center-line">OT SERVICES</p>
    <p class="brand-phone center-line">(555) 014-2087</p>

    <p class="question question--pink">Does your child struggle<br>with Reading/Kriah?</p>
    <p class="question question--yellow">Knows the information<br>but fails the test?</p>
    <p class="question question--green">Has difficulty remembering<br>names and dates?</p>

    <h2 class="promise center-line">YES YOUR CHILD <span class="struck">CAN</span> WILL<br>SUCCEED IN SCHOOL!</h2>

    <div class="service service--evaluate">
      <p class="service-title">WE EVALUATE:</p>
      <p class="service-text">Using standardized<br>Evaluations</p>
    </div>

    <svg class="pencil-art" role="img" aria-label="Education graphic: a sharpened pencil with pink, blue and green stripes" viewBox="0 0 80 164" preserveAspectRatio="none">
      <defs>
        <linearGradient id="pencil-fill" x1="0" y1="0" x2="0" y2="1">
          <stop offset="0" stop-color="#2a66c4"/>
          <stop offset="0.35" stop-color="#1aa3e0"/>
          <stop offset="0.7" stop-color="#8fd4f2"/>
          <stop offset="1" stop-color="#ffffff"/>
        </linearGradient>
      </defs>
      <rect x="0" y="0" width="80" height="164" fill="url(#pencil-fill)"/>
    </svg>

    <div class="service service--treat">
      <p class="service-title">WE TREAT:</p>
      <p class="service-text">Using Researched<br>based techniques</p>
    </div>

    <p class="approach center-line">We Treat theunderlying processing deficits</p>

    <p class="rsa-pill">Board of Ed OT RSA's accepted</p>

    <p class="details center-line">Located in<br>Borough Park Evaluations done in Borough Park &amp; Staten Island<br>For more information or to be added to our email list,<br>please email: brightpathot@example.com</p>

    <div class="footer-band">DANA HALLOWAY OTR/L<br>(555)014-2087</div>
  </div>
</body>
</html>
```